Noche de Salsa

We need a poster to promote a party. It is a salsa night at La Tortuga, a fun night out to dance, be with friends and have a few drinks. It is an informal occasion. The drinks will not be expensive and the snack will be typical mexican food.
La Tortuga is a campus for 8 local non-profit organizations but it also has high quality event venues and outdoor areas.
We would like a file for print (11x17") and a digital file for social media.
Enclosed:
- File with poster contents in spanish.
- La Tortuga logo
- Picture of palm trees at La Tortuga (you don't have to include this if another graphic fits best.
- Pic of the outside of the restaurant, where the dancing will take place. The restaurante is right in fron of the beach. THIS PICTURE DOES NOT NECESSARILY NEEDS TO BE PART OF THE POSTER.
- La Tortuga Fact Sheet for context.
Target Market(s)
Men and women from 25 to 50 years old.
American and mexican citizens.
Industry/Entity Type
Non-Profit
Colors
Designer to choose colors to be used in the design.
Look and feel
Each slider illustrates characteristics of the customer's brand and the style your logo design should communicate.

```html
<!DOCTYPE html>
<html lang="es">
<head>
<meta charset="utf-8">
<title>Noche de Salsa – La Tortuga</title>
<link rel="stylesheet" href="https://fonts.googleapis.com/css2?family=Great+Vibes&family=Montserrat:wght@600&family=Roboto+Condensed:ital,wght@0,300;0,400;0,700;1,300&display=swap">
<style>
  :root {
    --page-bg: #1e1712;
    --poster-top: #6b7650;
    --poster-mid: #4f5c3b;
    --poster-deep: #36422a;
    --cream: #e9dfa6;
    --cream-soft: #d8cf9c;
    --orange: #f0733d;
    --orange-light: #ff9a63;
    --orange-band: #e26a34;
    --white: #ffffff;
  }
  * { margin: 0; padding: 0; box-sizing: border-box; }
  html, body { width: 1200px; height: 1000px; overflow: hidden; }
  body { background: var(--page-bg); position: relative; font-family: "Roboto Condensed", sans-serif; }

  .poster {
    position: absolute; left: 301px; top: 37px; width: 598px; height: 923px;
    overflow: hidden;
    background: linear-gradient(180deg, var(--poster-top) 0%, var(--poster-mid) 45%, var(--poster-deep) 100%);
    box-shadow: 0 6px 24px rgba(0,0,0,.6);
  }
  .hero-photo {
    position: absolute; left: 0; top: 0; width: 598px; height: 330px;
    background:
      linear-gradient(180deg, rgba(0,0,0,0) 60%, var(--poster-top) 100%),
      linear-gradient(90deg, rgba(0,0,0,0) 58%, #c2562c 60%, #b24a27 85%, #7a3a22 100%),
      linear-gradient(180deg, #5b4a78 0%, #c06a5a 22%, #3c3438 38%, #6d7a62 55%, #9a9d92 80%);
  }
  .hero-glow {
    position: absolute; left: 0; top: 230px; width: 598px; height: 200px;
    background: radial-gradient(ellipse at 50% 40%, rgba(230,240,200,.35), rgba(0,0,0,0) 65%);
  }

  .title-script {
    position: absolute; top: 300px; width: 100%; text-align: center;
    font-family: "Great Vibes", cursive; font-size: 66px; color: var(--cream);
    text-shadow: 0 2px 4px rgba(0,0,0,.35);
  }
  .title-main {
    position: absolute; top: 352px; width: 100%; text-align: center;
    font-family: "Montserrat", sans-serif; font-weight: 600; font-size: 138px; letter-spacing: -2px;
    line-height: 1;
    background: linear-gradient(180deg, var(--orange-light), var(--orange));
    -webkit-background-clip: text; background-clip: text; color: transparent;
    filter: drop-shadow(0 3px 4px rgba(0,0,0,.35));
  }

  .date-row {
    position: absolute; top: 482px; left: 0; width: 100%;
    display: flex; align-items: center; gap: 10px;
  }
  .date-row .rule { flex: 1; height: 2px; background: var(--orange); }
  .date {
    font-weight: 700; font-size: 25px; color: var(--cream); white-space: nowrap;
  }
  .entry {
    position: absolute; top: 515px; width: 100%; text-align: center;
    font-size: 15px; color: var(--cream-soft);
  }
  .entry .arrow { color: var(--cream); font-size: 11px; margin: 0 4px; }
  .entry em { font-style: italic; font-weight: 300; font-size: 12px; }

  .venue-name {
    position: absolute; top: 620px; width: 100%;
    display: flex; justify-content: center; align-items: center; gap: 12px;
    font-weight: 400; font-size: 50px; color: var(--white); line-height: 1;
  }
  .venue-name .dot { width: 22px; height: 22px; border-radius: 50%; background: var(--white); }

  .address-main {
    position: absolute; top: 686px; width: 100%; text-align: center;
    font-weight: 700; font-size: 32px; color: var(--cream);
  }
  .address-sub {
    position: absolute; top: 726px; width: 100%; text-align: center;
    font-weight: 400; font-size: 24px; color: var(--cream);
  }
  .address-note {
    position: absolute; top: 757px; width: 100%; text-align: center;
    font-style: italic; font-weight: 300; font-size: 11px; color: var(--cream-soft);
  }

  .info-band {
    position: absolute; left: 0; top: 803px; width: 239px; height: 26px;
    background: var(--orange-band);
    font-weight: 300; font-size: 15px; color: #ffe1cc;
    text-align: right; padding-right: 10px; line-height: 26px;
  }
  .phone {
    position: absolute; left: 260px; top: 812px;
    font-weight: 400; font-size: 23px; color: var(--white);
  }
  .phone svg { vertical-align: -3px; margin-right: 4px; }
  .email {
    position: absolute; left: 190px; top: 838px;
    font-size: 30px; color: var(--cream);
  }
  .email strong { font-weight: 700; color: var(--orange-light); }
  .email span { font-weight: 400; }
</style>
</head>
<body>
  <main class="poster">
    <div class="hero-photo" role="img" aria-label="Fotografía de una pareja bailando salsa en la terraza del restaurante, con palmeras al atardecer y trazos de luz"></div>
    <div class="hero-glow"></div>

    <h1>
      <span class="title-script">Noche de</span>
      <span class="title-main">SALSA</span>
    </h1>

    <div class="date-row">
      <span class="rule"></span>
      <span class="date">VIERNES, 14 DE NOVIEMBRE 2014</span>
      <span class="rule"></span>
    </div>
    <p class="entry">ENTRADA <span class="arrow">▶</span> $100 pesos <em>(Incluye 1 bebida)</em></p>

    <div class="venue-name"><span class="dot"></span>la tortuga</div>

    <p class="address-main">Acceso Costero #1480</p>
    <p class="address-sub">Col. Las Palmas, C.P. 23999, Bahía Clara, B.C.S.</p>
    <p class="address-note">(al final de la calle Palmar, junto al antiguo muelle)</p>

    <div class="info-band">más informes al</div>
    <p class="phone">555-0148</p>
    <p class="email"><strong>Info</strong><span>@</span><strong>laTortuga</strong><span>.org</span></p>
  </main>
</body>
</html>
```